female stress management consultant, doctor, Health & Well-being coach needs a wordpress theme

I am a Stress management consultant, General Practitioner and Health and Well-Being coach who is targeting mainly surgeries/hospitals and corporate business.
I have my own URL drhalvoreskby.com and the hosting.
I need a WordPress Website that is easy to maintain and edit to regularly change the content (copy/pictures/action buttons/banners).
I want my website to look professional and elegant for corporate businesses and managers to feel they can trust me and my expertise. At the same time, the website should have a warm and welcoming feel to it. It should feel uplifting and very positive.
I am open to colour suggestions, but please incorporate the following two colours: #F18877 and #D2BB7A. For fonts I prefer grey over black (like #777777).
The website needs to create an impression of "know like and trust".
The website should have a sign-up button for a newsletter, multiple contact buttons over the home page - to write an email to me, contact details top and bottom and the possibility to have a video on the home page top instead of a picture (Best would be that I can change from picture to video to picture in the future without needing a designer). A video that can run in the background with text laid over. A bit like on this website from Tessa Grublin: https://www.tessagrublin.com.
I need 5 pages: Home, About, Services, Contact, free resources. I do NOT need an e-commerce or booking facility as I will neither sell nor let people book through my website. I don't need a blog either.
All the pages need to have a link to my other website (brightpathdaily.co.uk) and it needs to state that the linked website (brightpathdaily) is my website with a blog and for private customers.
Please use the photos I attached if possible. Me with the dogs for the "about" section.

Websites I like: https://www.orlaqvx.com, tessagrublin.com, https://pennyrastrick.com (this site is too dark for my liking, but the layout has a simple navigation layout, the important buttons are right up at the side (LinkedIn/social media/CTA), is minimalistic - hence easy to find the important bits).

surgeries/doctor offices, hospitals, corporate business

Health and well-being

• see project description
• see project description

```html
<!DOCTYPE html>
<html lang="en">
<head>
<meta charset="utf-8">
<title>Dr Halvor Eskby – Health &amp; Well-being</title>
<link href="https://fonts.googleapis.com/css2?family=Poppins:wght@400;500;600;700;800&family=Roboto:wght@400;500;700&family=Allura&display=swap" rel="stylesheet">
<style>
:root{
  --salmon:#F18877;
  --salmon-soft:#f4a99c;
  --gold:#D2BB7A;
  --ink:#222222;
  --grey:#777777;
  --white:#ffffff;
  --cream:#f7f3ea;
}
*{box-sizing:border-box;margin:0;padding:0}
html,body{width:1200px;height:3830px;overflow:hidden}
body{position:relative;background:var(--white);font-family:'Poppins',sans-serif;color:var(--grey)}
.abs{position:absolute}
.script{font-family:'Allura',cursive;color:var(--salmon);font-weight:400}

/* header */
.brand{left:100px;top:40px;width:180px;text-align:center}
.brand-dot{display:block;width:38px;height:38px;border-radius:50%;background:var(--salmon);margin:0 auto 8px}
.brand-name{font-size:17px;color:var(--salmon);font-weight:400;display:block}
.brand-tag{font-size:8px;color:var(--salmon);display:block;margin-top:2px}
.nav{left:456px;top:38px;display:flex;gap:27px;font-size:14px;font-weight:500;color:var(--ink);z-index:3}
.nav .active{color:var(--salmon)}
.nav-divider{left:926px;top:36px;width:1px;height:28px;background:#999;z-index:3}
.socials{display:flex;gap:8px;z-index:3}
.socials span{width:27px;height:27px;border:1.5px solid var(--ink);border-radius:50%;display:block}

/* hero */
.hero-photo{left:0;top:0;width:1200px;height:700px;background:linear-gradient(180deg,#cfe3ee 0%,#e7eef0 35%,#8fbfd0 55%,#d9cdb4 100%)}
.hero-title{left:690px;top:192px;width:265px;text-align:center;font-size:49px;line-height:52px;font-weight:700;color:var(--ink);z-index:2}
.hero-script{left:760px;top:410px;font-size:90px;z-index:3}
.round-btn{width:40px;height:40px;border-radius:50%;background:var(--white);box-shadow:0 2px 6px rgba(0,0,0,.15);display:flex;align-items:center;justify-content:center}

/* how I help */
.help-title{left:0;width:1200px;top:850px;text-align:center;font-size:38px;font-weight:700;color:var(--ink)}
.help-title .script{font-size:80px;margin-left:6px}
.service-photo{top:949px;width:472px;height:315px;border-radius:6px}
.service-btn{top:1217px;width:408px;height:89px;border-radius:14px;background:var(--salmon);color:var(--white);font-weight:700;font-size:21px;display:flex;align-items:center;justify-content:center;text-align:center;line-height:30px;padding:0 40px}

/* about */
.about-card{left:112px;top:1413px;width:976px;height:535px;background:var(--white);box-shadow:0 2px 12px rgba(0,0,0,.08);z-index:2}
.about-photo{left:170px;top:1488px;width:378px;height:378px;border-radius:50%;background:radial-gradient(circle at 45% 40%,#c9b48f,#6f8d5a 70%,#556b45);z-index:3}
.about-ring{left:153px;top:1471px;width:412px;height:412px;border-radius:50%;border:2px dashed var(--salmon);z-index:3}
.about-text{left:584px;top:1470px;width:458px;z-index:3}
.about-text h2{font-size:38px;font-weight:700;color:var(--ink)}
.about-text h2 .script{font-size:70px;margin-left:8px}
.about-text h3{font-size:17px;line-height:26px;font-weight:600;color:var(--ink);margin-top:4px;text-align:justify}
.about-text p{font-size:14px;line-height:26px;margin-top:14px;text-align:justify}

/* testimonials */
.testi-title{left:0;width:1200px;top:2020px;text-align:center;font-size:38px;font-weight:700;color:var(--white);z-index:2}
.testi-card{top:2094px;height:187px;border-radius:40px;font-size:14px;line-height:22px;text-align:center;padding:30px 46px;z-index:2}
.testi-main{left:265px;width:670px;background:var(--white)}
.testi-main strong{display:block;color:var(--ink);font-weight:600;margin-bottom:10px}
.testi-side{background:var(--salmon-soft);color:#a15a4e;width:250px}
.avatar{left:550px;top:2233px;width:102px;height:102px;border-radius:50%;border:3px solid var(--white);background:radial-gradient(circle at 50% 45%,#f3c764,#d98d2e 55%,#5a3a1e);z-index:3}
.testi-name{left:0;width:1200px;top:2345px;text-align:center;color:var(--white);font-size:20px;font-weight:700;z-index:2}
.testi-role{left:0;width:1200px;top:2375px;text-align:center;color:var(--white);font-size:14px;z-index:2}

/* self-care */
.care-text{left:112px;top:2596px;width:490px}
.care-text h2{font-size:35px;line-height:44px;font-weight:700;color:var(--ink)}
.care-text h2 em{font-style:normal;color:var(--salmon)}
.care-text p{font-size:14px;line-height:26px;margin-top:20px;text-align:justify}
.btn-gold{display:inline-block;margin-top:22px;background:var(--gold);color:var(--white);font-weight:600;font-size:13px;padding:12px 35px;border-radius:22px;margin-left:3px}
.care-photo{left:620px;top:2605px;width:520px;height:550px;border-radius:48% 52% 46% 54%/52% 48% 52% 48%;background:radial-gradient(circle at 50% 45%,#e5c3a9,#c99f83 45%,#f5efe3 75%,rgba(255,255,255,0) 100%)}

/* footer */
.foot-brand{left:500px;top:3425px;width:200px;text-align:center;color:var(--white);z-index:2}
.foot-brand .brand-dot{background:var(--white)}
.foot-brand .brand-name,.foot-brand .brand-tag{color:var(--white)}
.foot-col{top:3574px;color:var(--white);font-family:'Roboto',sans-serif;font-size:15px;line-height:26px;z-index:2}
.foot-col h4{font-size:18px;font-weight:700;margin-bottom:12px;line-height:24px}
.contact-row{display:flex;gap:12px;align-items:flex-start}
.contact-row svg{flex:none;margin-top:5px}
.news-form{display:flex;gap:5px;margin-top:14px}
.news-input{width:278px;height:36px;background:var(--white);border-radius:18px;color:#555;font-size:13px;padding:9px 26px}
.news-btn{width:115px;height:36px;background:var(--gold);border-radius:18px;font-size:13px;font-weight:700;text-align:center;padding-top:9px}
.foot-socials{margin-top:16px}
.foot-socials span{border-color:var(--white)}
.copyright{left:0;width:1200px;top:3788px;text-align:center;color:var(--white);font-family:'Roboto',sans-serif;font-size:14px;z-index:2}
</style>
</head>
<body>

<!-- hero -->
<div class="abs hero-photo" role="img" aria-label="Smiling woman in a straw hat on a sunny beach"></div>
<svg class="abs" style="left:0;top:510px;z-index:1" width="1200" height="270" viewBox="0 0 1200 270">
  <path d="M0 70 C120 40 260 85 420 95 C560 100 620 110 780 80 C920 55 1060 45 1200 20 L1200 115 C1050 150 950 180 820 200 C700 220 560 230 460 265 C420 240 320 225 200 170 C120 140 50 120 0 110 Z" fill="var(--gold)"/>
</svg>
<div class="abs brand" style="z-index:3"><span class="brand-dot"></span><span class="brand-name">Dr Halvor Eskby</span><span class="brand-tag">Create a life you love living</span></div>
<nav class="abs nav"><span class="active">Home</span><span>About us</span><span>Services</span><span>Contact</span><span>Free Resources</span></nav>
<div class="abs nav-divider"></div>
<div class="abs socials" style="left:956px;top:37px"><span></span><span></span><span></span><span></span></div>
<h1 class="abs hero-title">UNLOCK THE POSITIVE POWER WITHIN</h1>
<div class="abs hero-script script">You</div>
<div class="abs round-btn" style="left:25px;top:330px;z-index:2"><svg width="12" height="12" viewBox="0 0 12 12"><path d="M8 1 3 6l5 5" stroke="#222" stroke-width="2" fill="none"/></svg></div>
<div class="abs round-btn" style="left:1124px;top:330px;z-index:2"><svg width="12" height="12" viewBox="0 0 12 12"><path d="M4 1l5 5-5 5" stroke="#222" stroke-width="2" fill="none"/></svg></div>

<!-- how I help -->
<h2 class="abs help-title">HOW I <span class="script">Help</span></h2>
<svg class="abs" style="left:40px;top:1108px" width="30" height="26"><path d="M0 13 26 0v26z" fill="#c9dedd"/></svg>
<svg class="abs" style="left:1130px;top:1108px" width="30" height="26"><path d="M30 13 4 0v26z" fill="#c9dedd"/></svg>
<div class="abs service-photo" style="left:112px;background:linear-gradient(135deg,#5f9aa3,#d8d2c6 60%,#eae4da)" role="img" aria-label="Woman writing notes in an armchair with a laptop"></div>
<div class="abs service-photo" style="left:616px;background:linear-gradient(135deg,#6b5a63,#3e4a5c 55%,#a6a39c)" role="img" aria-label="Two women talking on a sofa in a consultation room"></div>
<div class="abs service-btn" style="left:144px">1:1 COACHING ONLINE OR IN PERSON</div>
<div class="abs service-btn" style="left:648px">TALKS &amp; WORKSHOPS</div>

<!-- salmon band -->
<svg class="abs" style="left:0;top:1720px" width="1200" height="760" viewBox="0 0 1200 760">
  <path d="M0 12 C60 20 120 40 200 60 L1000 60 C1080 40 1140 20 1200 10 L1200 660 C1080 650 980 650 860 690 C760 715 660 720 600 755 C540 720 420 700 300 690 C180 680 80 690 0 700 Z" fill="var(--salmon)"/>
</svg>

<!-- about -->
<div class="abs about-card"></div>
<div class="abs about-ring"></div>
<div class="abs about-photo" role="img" aria-label="Doctor sitting outdoors with her two dogs"></div>
<div class="abs about-text">
  <h2>ABOUT <span class="script">Me</span></h2>
  <h3>Unlock the Power of Joy and Well-Being: Discover Simple Steps to Restore Your Happiness and Health Today!</h3>
  <p>With over 30 years of being a doctor, I've met countless people facing ongoing health issues and struggles that couldn't be solved solely through conventional medicine. That's why it's so important to embrace a holistic approach in our quest for balance, shifting from discomfort to vitality and contentment.</p>
  <p>The secret to living a joyful, vibrant life lies in nurturing every aspect of yourself, not just your physical body. Surprisingly, it's easier as you might think to harmonize your body, mind, and spirit and experience optimal well-being.</p>
</div>

<!-- testimonials -->
<h2 class="abs testi-title">TESTIMONIALS</h2>
<div class="abs testi-card testi-side" style="left:-10px;text-align:left;padding:30px 20px">more. For what I am. The sessions with Halvor's understanding of an exclusive, supportive and</div>
<div class="abs testi-card testi-main"><strong>"I feel more positive and stopped procrastination."</strong>Working with Dr Halvor has helped me stay more positive and helped me to stop procrastination. I feel more connected to my True Self - the True Self we loose as we progress through life. I felt very relaxed and positive after each session.</div>
<div class="abs testi-card testi-side" style="left:960px;text-align:left;padding:30px 30px 30px 52px">The workshop has allowed quality of delivery is what made the guided meditations help</div>
<div class="abs round-btn" style="left:70px;top:2171px;z-index:3"><svg width="12" height="12" viewBox="0 0 12 12"><path d="M8 1 3 6l5 5" stroke="#222" stroke-width="2" fill="none"/></svg></div>
<div class="abs round-btn" style="left:1090px;top:2171px;z-index:3"><svg width="12" height="12" viewBox="0 0 12 12"><path d="M4 1l5 5-5 5" stroke="#222" stroke-width="2" fill="none"/></svg></div>
<div class="abs avatar" role="img" aria-label="Silhouette of a person with open arms at sunset"></div>
<div class="abs testi-name">Nadia Pellworth</div>
<div class="abs testi-role">Counsellor, Hypnotherapist, Reiki master, Reflexologist</div>

<!-- self-care -->
<div class="abs care-photo" role="img" aria-label="Portrait of the doctor smiling"></div>
<div class="abs care-text">
  <h2><em>Revitalise Your Life with Ease:</em> Master the Art of Self-Care in Simple, yet Powerful Ways!</h2>
  <p>Feeling exhausted, overwhelmed, and constantly drained of energy? It's time to break free from the burdens that weigh you down. Have you experienced unexplained irritability, tearfulness, or a persistent feeling of being down? You know deep down that this isn't the real you. It's time to reclaim your vitality and joy.</p>
  <p>If you're tired of seeking answers in conventional medicine without success, you're not alone. Many people face similar struggles. But the solution often lies in taking a holistic approach, considering all aspects of your well-being and the factors that have led to your current state. Let's uncover the secrets to a life filled with joy and vitality.</p>
  <span class="btn-gold">START YOUR EXCITING FUTURE</span>
</div>

<!-- footer -->
<svg class="abs" style="left:0;top:3245px" width="1200" height="585" viewBox="0 0 1200 585">
  <path d="M0 170 C150 120 250 60 340 50 C460 40 540 60 600 30 C700 50 780 40 900 20 C1000 5 1100 10 1200 0 L1200 200 L0 230 Z" fill="var(--gold)"/>
  <path d="M0 225 C200 200 380 160 600 165 C820 160 1000 190 1200 170 L1200 585 L0 585 Z" fill="var(--salmon)"/>
</svg>
<div class="abs foot-brand"><span class="brand-dot"></span><span class="brand-name">Dr Halvor Eskby</span><span class="brand-tag">Create a life you love living</span></div>
<div class="abs foot-col" style="left:111px"><h4>Quick links</h4>Home<br>About<br>Services<br>Contact</div>
<div class="abs foot-col" style="left:320px;width:240px">
  <h4>Contact Us</h4>
  <div class="contact-row"><svg width="18" height="18" viewBox="0 0 18 18"><circle cx="9" cy="9" r="9" fill="#fff"/><path d="M9 4a3 3 0 0 0-3 3c0 2.4 3 6 3 6s3-3.6 3-6a3 3 0 0 0-3-3z" fill="var(--salmon)"/></svg><span>123,Lorem ipsum dolor sit a met, consectetur</span></div>
  <div class="contact-row"><svg width="18" height="18" viewBox="0 0 18 18"><circle cx="9" cy="9" r="9" fill="#fff"/><path d="M6 5l2 2-1 1c.6 1.2 1.6 2.2 2.8 2.8l1-1 2 2-1.3 1.3C8.5 12.6 5.4 9.5 4.7 6.3z" fill="var(--salmon)"/></svg><span>+1 888 888 8888</span></div>
  <div class="contact-row"><svg width="18" height="18" viewBox="0 0 18 18"><circle cx="9" cy="9" r="9" fill="#fff"/><rect x="5" y="6" width="8" height="6" fill="var(--salmon)"/><path d="M5 6l4 3 4-3" stroke="#fff" fill="none"/></svg><span>info@companyname.com</span></div>
</div>
<div class="abs foot-col" style="left:645px;width:420px">
  <h4>Get Regular Inspiration For Health, Wellbeing And Happiness</h4>
  <div class="news-form"><div class="news-input">Email address</div><div class="news-btn">Signup</div></div>
  <div class="socials foot-socials"><span></span><span></span><span></span><span></span></div>
</div>
<div class="abs copyright">© Copyright @2023 Company name | All Rights Reserved</div>

</body>
</html>
```